Business Card for boutique psychology business

Business card for boutique psychology practice in Melbourne. I want them to be relatively simply with the logo and backing colour taking up the front side. Then, text on the back, with my name; professional title (Clinical Psychologist); website - torvinpsychology.com.au; email: hello@torvinpsychology.com.au; insta: @torvin.psychology.emdr
Back should also have the words: Listen. Restore. Grow
Fonts used for logo are: Mikea Demo and Gotham Medium. Use something for back text that will compliment these.
Brand colours uploaded below. I'd like to see options in both olive and blush.

```html
<!DOCTYPE html>
<html lang="en">
<head>
<meta charset="utf-8">
<title>Torvin Psychology — Business Cards</title>
<link href="https://fonts.googleapis.com/css2?family=Montserrat:wght@400;500&family=Italiana&display=swap" rel="stylesheet">
<style>
  :root {
    --backdrop: #3a3a3b;
    --olive: #454a2f;
    --blush: #ecd0c1;
    --card-shadow: rgba(0,0,0,0.45);
  }
  * { margin: 0; padding: 0; box-sizing: border-box; }
  html, body {
    width: 1200px; height: 689px; overflow: hidden;
    background: var(--backdrop);
  }
  .sheet {
    position: relative; width: 1200px; height: 689px;
    display: flex; align-items: center; justify-content: center; gap: 60px;
  }
  .card {
    width: 500px; height: 286px; border-radius: 22px;
    position: relative;
    box-shadow: 0 18px 40px var(--card-shadow);
    font-family: "Montserrat", sans-serif;
  }
  .card--front { background: var(--olive); color: var(--blush); }
  .card--back { background: var(--blush); color: var(--olive); }

  .wordmark {
    font-family: "Montserrat", sans-serif;
    font-weight: 500;
    letter-spacing: 0.02em;
    line-height: 1;
    display: flex; align-items: center; gap: 12px;
  }
  .wordmark__dot {
    border-radius: 50%; background: currentColor; flex: none;
  }
  .card--front .wordmark {
    position: absolute; left: 0; right: 0; top: 86px;
    justify-content: center; font-size: 76px;
  }
  .card--front .wordmark__dot { width: 14px; height: 14px; }
  .motto {
    position: absolute; left: 0; right: 0; bottom: 44px;
    text-align: center; font-size: 13px; letter-spacing: 0.06em; font-weight: 400;
  }

  .card--back .wordmark {
    position: absolute; left: 40px; top: 36px; font-size: 46px;
  }
  .card--back .wordmark__dot { width: 10px; height: 10px; }
  .holder { position: absolute; left: 40px; top: 116px; }
  .holder__name {
    font-family: "Italiana", serif; font-size: 30px; letter-spacing: 0.06em;
    text-transform: uppercase; line-height: 1.05;
  }
  .holder__title { font-size: 14px; font-weight: 400; margin-top: 4px; letter-spacing: 0.02em; }
  .contact {
    position: absolute; left: 40px; top: 184px; list-style: none;
    font-size: 13px; line-height: 21px;
  }
  .contact li { display: flex; align-items: center; gap: 10px; }
  .contact svg { width: 12px; height: 12px; flex: none; }
</style>
</head>
<body>
<main class="sheet">
  <section class="card card--front" aria-label="Card front">
    <div class="wordmark"><span class="wordmark__dot"></span>torvin</div>
    <p class="motto">Listen. Restore. Grow</p>
  </section>

  <section class="card card--back" aria-label="Card back">
    <div class="wordmark"><span class="wordmark__dot"></span>torvin</div>
    <div class="holder">
      <p class="holder__name">Mara&nbsp;&nbsp;Ellison</p>
      <p class="holder__title">Clinical Psychologist</p>
    </div>
    <ul class="contact">
      <li>
        <svg viewBox="0 0 24 24" fill="currentColor" aria-hidden="true"><path d="M6.6 10.8a15 15 0 0 0 6.6 6.6l2.2-2.2c.3-.3.7-.4 1-.2 1.1.4 2.3.6 3.6.6.6 0 1 .4 1 1V20c0 .6-.4 1-1 1A17 17 0 0 1 3 4c0-.6.4-1 1-1h3.5c.6 0 1 .4 1 1 0 1.3.2 2.5.6 3.6.1.3 0 .7-.2 1z"/></svg>
        (03) 5550 1487
      </li>
      <li>
        <svg viewBox="0 0 24 24" fill="currentColor" aria-hidden="true"><path d="M2 5h20v14H2z M3.5 6.5 12 13l8.5-6.5" stroke="var(--blush)" stroke-width="1.5"/></svg>
        hello@torvinpsychology.com.au
      </li>
      <li>
        <svg viewBox="0 0 24 24" fill="none" stroke="currentColor" stroke-width="2" aria-hidden="true"><circle cx="12" cy="12" r="9"/><path d="M3 12h18M12 3c3 3 3 15 0 18M12 3c-3 3-3 15 0 18"/></svg>
        www.torvinpsychology.com.au
      </li>
      <li>
        <svg viewBox="0 0 24 24" fill="none" stroke="currentColor" stroke-width="2" aria-hidden="true"><rect x="3" y="3" width="18" height="18" rx="5"/><circle cx="12" cy="12" r="4"/></svg>
        @torvin.psychology.emdr
      </li>
    </ul>
  </section>
</main>
</body>
</html>
```